Design graphics and Print for a line of Herb Seeds- Envelope Design

We need a set of herb seed envelopes designed for a new seed line we are launching.
The design will be both front and back

Envelope will be a colored ( green) ) envelope with white text
or a white or cream envelope in all black /and images text. Or can add some colors to the white envelope.

I have attached the die-cut of the seed envelope.
I have attached some images of envelopes I like. Please do not copy, these are just to give you an idea of what I like.

Please feel free to reach out to me if you have any questions.

Thank you

Target Market(s)

The design needs to classic that can translate to 3 different audiences. 1. young parents 2. hip, young single millennial 3. kids

Industry/Entity Type

Ecommerce

Font styles to use
Serif

Requirements
Must have
• Please use the herb - Parsley for the design
Icon, Text or both.

Front side must have:
1.either herb Icon or work Parsley or both- this will be the main attraction
2. company name- Tall Meadow Pantry
3. can use design elements
4. can use my logo on from or back or not at all. I

Backside must have:
1. social media tags
FB, Lumo and Tackly ( use icons) @tallmeadowpantry

my website: www.tallmeadowpantry.example
this can be on from or back of the envelope.
Should not have
• please stay away from "county" flowery, old fashioned style designs

```html
<!DOCTYPE html>
<html lang="en">
<head>
<meta charset="utf-8">
<title>Tall Meadow Pantry – Parsley Seed Envelope Die Layout</title>
<link href="https://fonts.googleapis.com/css2?family=EB+Garamond:wght@400;500&display=swap" rel="stylesheet">
<style>
  :root {
    --paper: #ffffff;
    --ink: #1f1f1f;
    --die-line: #2a2a2a;
    --guide-blue: #a9d6f0;
    --reg-blue: #1aa3e8;
    --sage: #dfe4d2;
    --leaf-ink: #3d4a34;
    --logo-ink: #4a4640;
  }
  html, body {
    margin: 0;
    padding: 0;
    width: 1200px;
    height: 900px;
    overflow: hidden;
    background: var(--paper);
  }
  .die-sheet {
    display: block;
    width: 1200px;
    height: 900px;
  }
  .sheet-frame { fill: none; stroke: var(--die-line); stroke-width: 2; }
  .cut-line { fill: none; stroke: var(--die-line); stroke-width: 2.5; stroke-linejoin: round; }
  .panel-line { fill: none; stroke: #555; stroke-width: 2; }
  .fold-line { fill: none; stroke: #333; stroke-width: 2; stroke-dasharray: 30 22; }
  .guide-line { fill: none; stroke: var(--guide-blue); stroke-width: 2.5; }
  .reg-mark { fill: var(--reg-blue); }
  .sage-area { fill: var(--sage); }
  .icon-line { fill: none; stroke: var(--ink); stroke-width: 2.5; }
  .network-dot { fill: none; stroke: var(--ink); stroke-width: 2.5; }
  .brand-title {
    font-family: "EB Garamond", Georgia, serif;
    font-size: 63px;
    fill: var(--ink);
  }
  .herb-name {
    font-family: "EB Garamond", Georgia, serif;
    font-size: 110px;
    letter-spacing: 2px;
    fill: var(--leaf-ink);
  }
  .herb-note {
    font-family: "EB Garamond", Georgia, serif;
    font-size: 28px;
    letter-spacing: 8px;
    fill: var(--leaf-ink);
  }
  .social-handle {
    font-family: "EB Garamond", Georgia, serif;
    font-size: 31px;
    fill: var(--ink);
  }
  .network-name {
    font-family: "EB Garamond", Georgia, serif;
    font-size: 22px;
    fill: var(--ink);
  }
  .seal-name {
    font-family: "EB Garamond", Georgia, serif;
    font-size: 21px;
    fill: var(--logo-ink);
  }
  .die-spec {
    font-family: "EB Garamond", Georgia, serif;
    font-size: 27px;
    fill: var(--ink);
  }
  .die-code { font-size: 32px; }
</style>
</head>
<body>
<svg class="die-sheet" viewBox="0 0 2212 1659" preserveAspectRatio="none" xmlns="http://www.w3.org/2000/svg">

  <rect class="sheet-frame" x="158" y="66" width="1925" height="1526"/>

  <g class="registration">
    <polygon class="reg-mark" points="205,66 220,97 190,97"/>
    <polygon class="reg-mark" points="158,97 190,110 158,128"/>
    <polygon class="reg-mark" points="2036,66 2051,97 2021,97"/>
    <polygon class="reg-mark" points="2083,97 2051,110 2083,128"/>
    <polygon class="reg-mark" points="205,1592 220,1561 190,1561"/>
    <polygon class="reg-mark" points="158,1530 190,1546 158,1561"/>
    <polygon class="reg-mark" points="2036,1592 2051,1561 2021,1561"/>
    <polygon class="reg-mark" points="2083,1530 2051,1546 2083,1561"/>
  </g>

  <g class="guides">
    <path class="guide-line" d="M697,293 H243 V1047"/>
    <path class="guide-line" d="M203,245 V1410"/>
    <path class="guide-line" d="M1040,66 V80 M1905,66 V80 M1040,1580 V1592 M1905,1580 V1592"/>
    <path class="guide-line" d="M158,245 H180 M158,1410 H180 M2060,232 H2083 M2060,1425 H2083"/>
    <path class="guide-line" d="M990,180 L1040,230 M1955,180 L1905,230 M990,1475 L1040,1425 M1955,1475 L1905,1425"/>
  </g>

  <g class="die-cut">
    <path class="cut-line" d="M1010,230 L1005,245 H285 Q208,245 208,322 V1335 Q208,1410 285,1410 H1010"/>
    <path class="cut-line" d="M1010,230 L1050,195 L1060,115 Q1063,90 1090,90 H1855 Q1880,90 1882,115 L1887,190 L1937,235"/>
    <path class="cut-line" d="M1100,197 V155 Q1100,132 1125,132 H1815 Q1840,132 1840,155 V197"/>
    <path class="cut-line" d="M1010,1425 L1050,1462 L1060,1540 Q1063,1565 1090,1565 H1855 Q1880,1565 1882,1540 L1887,1465 L1937,1425"/>
    <path class="cut-line" d="M1100,1462 V1505 Q1100,1528 1125,1528 H1815 Q1840,1528 1840,1505 V1462"/>
    <path class="cut-line" d="M1937,235 L1945,247 H2000 Q2045,250 2045,295 V1365 Q2045,1405 2000,1408 H1945 L1937,1425"/>
    <rect class="panel-line" x="1010" y="200" width="927" height="1260"/>
    <rect class="panel-line" x="1937" y="398" width="66" height="860"/>
  </g>

  <g class="front-panel">
    <rect class="fold-line" x="1042" y="232" width="862" height="1193"/>
    <rect class="panel-line" x="1073" y="264" width="795" height="1127"/>

    <g class="hero-herb" role="img" aria-label="Parsley sprig in line art over a soft sage blob">
      <path class="sage-area"
        d="M1380,545 C1480,510 1600,560 1680,700 C1760,840 1740,990 1640,1040 C1570,1070 1510,1060 1480,1080 C1520,1120 1510,1170 1420,1170 C1320,1170 1280,1080 1290,1000 C1260,900 1240,780 1255,700 C1265,620 1310,565 1380,545 Z"/>
      <text class="herb-name" x="1492" y="840" text-anchor="middle">Parsley</text>
      <text class="herb-note" x="1492" y="890" text-anchor="middle">HERB SEEDS</text>
    </g>

    <path class="sage-area" role="img" aria-label="Small parsley leaf cluster in the top corner"
      d="M1705,300 Q1760,280 1810,300 Q1805,355 1780,380 Q1740,375 1715,350 Q1702,325 1705,300 Z"/>
    <path class="sage-area" role="img" aria-label="Scattered parsley seeds beside the name"
      d="M1132,425 Q1160,412 1190,425 Q1192,452 1162,456 Q1134,450 1132,425 Z"/>
    <path class="sage-area" role="img" aria-label="Parsley leaf cluster in the bottom corner"
      d="M1110,1225 Q1160,1195 1205,1230 Q1230,1290 1215,1330 Q1175,1345 1135,1335 Q1105,1300 1110,1225 Z"/>

    <text class="brand-title" x="1198" y="432">Tall Meadow Pantry</text>

    <g class="brand-seal">
      <circle cx="1763" cy="1285" r="66" fill="none" stroke="var(--logo-ink)" stroke-width="3"/>
      <text class="seal-name" x="1763" y="1278" text-anchor="middle">Tall Meadow</text>
      <text class="seal-name" x="1763" y="1304" text-anchor="middle">Pantry</text>
    </g>
  </g>

  <g class="back-panel">
    <rect class="panel-line" x="344" y="398" width="663" height="863"/>

    <g class="social-row">
      <circle class="network-dot" cx="434" cy="583" r="12"/>
      <text class="network-name" x="453" y="591">Kinlo</text>
      <text class="social-handle" x="535" y="592">@tallmeadowpantry</text>
    </g>
    <g class="social-row">
      <circle class="network-dot" cx="434" cy="694" r="12"/>
      <text class="network-name" x="453" y="702">Lumo</text>
      <text class="social-handle" x="535" y="703">@tallmeadowpantry</text>
    </g>
    <g class="social-row">
      <circle class="network-dot" cx="434" cy="805" r="12"/>
      <text class="network-name" x="453" y="813">Tackly</text>
      <text class="social-handle" x="535" y="814">@tallmeadowpantry</text>
    </g>
    <g class="social-row">
      <ellipse class="sage-area" cx="445" cy="905" rx="28" ry="24"/>
      <g class="web-icon">
        <circle class="icon-line" cx="458" cy="917" r="36"/>
        <ellipse class="icon-line" cx="458" cy="917" rx="15" ry="36"/>
        <path class="icon-line" d="M458,881 V953 M422,917 H494 M428,898 H488 M428,936 H488"/>
      </g>
      <text class="social-handle" x="535" y="925">www.tallmeadowpantry.example</text>
    </g>

    <path class="sage-area" role="img" aria-label="Parsley sprig with scattered seeds"
      d="M725,1150 Q770,1135 800,1160 Q795,1185 765,1190 Q730,1180 725,1150 Z M860,1090 Q905,1075 945,1100 Q945,1125 910,1125 Q870,1120 860,1090 Z"/>
  </g>

  <g class="die-info">
    <circle cx="306" cy="1508" r="40" fill="none" stroke="var(--die-line)" stroke-width="2.5"/>
    <path d="M244,1508 H368 M306,1462 V1560" stroke="var(--die-line)" stroke-width="2"/>
    <circle cx="306" cy="1508" r="10" fill="var(--die-line)"/>
    <text class="die-spec" x="374" y="1490">Die: <tspan class="die-code">2BA</tspan> 3.25 x 4.5  (3 1/4 W x 4 1/2 H)</text>
  </g>
</svg>
</body>
</html>
```